zVerda Corporate Website

zVerda is a well-funded start up developing an Online Marketing Platform for small businesses in Europe.
We are launching in February 2012 with all-in-one online marketing services including professional website, DIY SEO, Dashboard with Reports and Online marketing tools, and Support.
Our internal web designer has come up with a preliminary website design which we wish to continue to improve using new ideas, colours, layout, image, etc.
The brief is very simple - improve the website whether it is look & feel, ease of use, conversion rate - we are looking for overall improvements.
The contest will last 5 days and we will award the winner £300.
If you are the winner , you will also be required to provide designs for 3 more internal pages adhering to the proposed home page design.
Judging criteria : -
Visual Design
Layout must adhere to best practices and wire frame. If you decide to move elements around significantly please provide reason
Functional, informative and drives calls to action
Industry/Entity Type
Marketing
Look and feel
Each slider illustrates characteristics of the customer's brand and the style your logo design should communicate.

```html
<!DOCTYPE html>
<html lang="en">
<head>
<meta charset="utf-8">
<title>zVerda – Online Marketing for Small Business</title>
<link rel="stylesheet" href="https://fonts.googleapis.com/css2?family=Arimo:wght@400;700&family=Noto+Serif:ital@1&display=swap">
<style>
:root{
  --blue:#2ba5d6;
  --blue-dark:#1c95c2;
  --heading-blue:#2a9fc9;
  --ink:#2b2b2b;
  --ink-soft:#555;
  --navy:#16364a;
  --red:#e8213f;
  --purple:#7b5c96;
  --green:#8dc63f;
  --grey-card:#a8a8a8;
  --band:#4a95c0;
  --panel:#ebebeb;
  --footer:#3a3a3a;
  --footer-text:#dcdcdc;
}
*{box-sizing:border-box;margin:0;padding:0}
html,body{width:978px;height:1200px;overflow:hidden}
body{position:relative;font-family:Arimo,Arial,sans-serif;color:var(--ink);background:#fff}
.abs{position:absolute}

/* header */
.header{position:absolute;left:0;top:0;width:978px;height:122px;background:#fff}
.tagline{left:645px;top:25px;font:italic 12px "Noto Serif",Georgia,serif;color:#333}
.brand{left:45px;top:48px;display:flex;align-items:center;gap:8px}
.brand-dot{width:42px;height:42px;border-radius:50%;background:var(--blue)}
.brand-name{font-size:38px;color:var(--ink-soft)}
.nav{left:397px;top:80px;width:445px;height:42px;border-radius:4px 4px 0 0;background:linear-gradient(#55c6ea,#2aa3d4);display:flex}
.nav a{flex:1;color:#fff;font-size:12.5px;text-decoration:none;display:flex;align-items:center;justify-content:center;border-left:1px solid rgba(0,0,0,.15)}
.nav a:first-child{border-left:none}
.login{left:868px;top:93px;font-size:17px;color:var(--ink)}

/* hero */
.hero{position:absolute;left:0;top:122px;width:978px;height:333px;background:linear-gradient(180deg,#28a7d8 0%,#4dbde7 60%,#2a9fd0 100%)}
.checklist{left:50px;top:30px;list-style:none}
.checklist li{display:flex;align-items:center;gap:12px;height:32.3px;font-size:17px;color:var(--navy)}
.hero-title{left:50px;top:188px;font-size:23px;line-height:29px}
.hero-title b{color:#3a4a52}
.hero-title span{color:#fff;font-weight:400}
.signup{left:99px;top:264px;font-size:12px;color:var(--navy)}
.free-btn{left:198px;top:256px;width:94px;height:30px;border-radius:3px;background:linear-gradient(#ffa43a,#f07f10);color:#fff;font-weight:700;font-size:17px;display:flex;align-items:center;justify-content:center}
.showcase{left:376px;top:26px;width:544px;height:278px;background:#fff;box-shadow:0 2px 6px rgba(0,0,0,.25)}
.showcase-art{position:absolute;left:268px;top:12px;width:266px;height:255px;background:radial-gradient(circle at 55% 45%,#f3c27a 0%,#9fc0de 35%,#f3f6f9 72%,#fff 100%)}
.showcase h2{position:absolute;left:22px;top:102px;font-size:16.5px;line-height:21px;color:var(--heading-blue);z-index:1}
.showcase p{position:absolute;left:22px;top:173px;font-size:14.5px;line-height:18px;color:var(--ink);z-index:1}

/* websites carousel */
.section-title{left:58px;top:474px;font-size:20px;font-weight:400;color:var(--ink)}
.arrow{top:576px}
.thumb{top:513px;width:143px;height:147px;background:#fff;border:1px solid #ddd;box-shadow:0 1px 4px rgba(0,0,0,.2);padding:5px}
.thumb div{width:100%;height:100%}
.quote{left:718px;top:512px;width:222px;font-size:14.6px;line-height:18.6px;color:#333}
.quote strong{font-size:18px}
.quote .mark{font-size:22px;font-weight:700}

/* offers */
.offer{top:692px;width:207px;height:137px;overflow:hidden;color:#fff}
.offer .price{position:absolute;right:-22px;top:-22px;width:84px;height:84px;border-radius:50%;background:var(--red);padding:30px 0 0 10px;font-weight:700;font-size:24px;line-height:20px}
.offer .price small{display:block;font-size:9px;text-align:right;padding-right:26px}
.offer .badge{position:absolute;border-radius:50%;background:#16a1df;color:#fff;font-weight:700;display:flex;align-items:center;justify-content:center;text-align:center;transform:rotate(-18deg)}
.offer .headline{position:absolute;font-weight:700;white-space:nowrap}
.offer .band{position:absolute;left:0;bottom:0;width:100%;height:28px;background:var(--band);font-size:11.5px;font-weight:700;display:flex;align-items:center;justify-content:center;text-align:center;line-height:11px;white-space:nowrap}
.how{left:713px;top:691px;width:225px;height:138px;background:var(--blue-dark);padding:14px 11px 14px 13px}
.how h3{font-size:18.5px;color:#1c3a4a;margin-bottom:6px}
.how p{font-size:14.2px;line-height:20px;color:#e6f4fa}

/* feature cards */
.features{position:absolute;left:0;top:850px;width:978px;height:150px;background:var(--panel)}
.card{top:10px;width:219px;height:110px;background:linear-gradient(#fff,#f2f2f2);border-radius:3px}
.card .icon{position:absolute;left:26px;top:10px}
.card h4{position:absolute;left:60px;top:16px;font-size:15px;font-weight:400;color:var(--ink)}
.card p{position:absolute;left:28px;top:47px;width:170px;font-size:11px;line-height:16px;color:#333}
.card a{position:absolute;right:14px;top:86px;font-size:11px;color:var(--blue);text-decoration:none}

/* footer */
.footer{position:absolute;left:0;top:1000px;width:978px;height:200px;background:var(--footer);color:var(--footer-text);font-size:11px}
.fcol{top:22px;border-left:1px solid #888;padding-left:12px;list-style:none}
.fcol li{line-height:22px}
.news-label{left:725px;top:25px;font-size:11px;color:#eee}
.news-input{left:724px;top:43px;width:200px;height:20px;background:#e4e4e4;font-size:9px;color:#333;padding:5px 6px}
.news-go{left:902px;top:42px}
.social{top:98px;width:19px;height:19px;border-radius:3px}
.rule{left:35px;top:137px;width:903px;height:1px;background:#777}
.copyright{left:0;top:169px;width:978px;text-align:center;font-size:9px;color:#ccc}
</style>
</head>
<body>

<header class="header">
  <p class="abs tagline"><u>Contact us</u> to join an exciting and well-funded start up</p>
  <div class="abs brand"><span class="brand-dot"></span><span class="brand-name">zVerda</span></div>
  <nav class="abs nav">
    <a href="#">Home</a><a href="#">About Us</a><a href="#">Quick Tour</a><a href="#">Pricing</a><a href="#">Contact Us</a>
  </nav>
  <span class="abs login">Login</span>
</header>

<section class="hero">
  <ul class="abs checklist">
    <li><svg width="20" height="18" viewBox="0 0 20 18"><rect x="1" y="4" width="13" height="13" fill="none" stroke="#16364a" stroke-width="2"/><path d="M4 9l4 4 10-12" fill="none" stroke="#16364a" stroke-width="3"/></svg>Business Websites</li>
    <li><svg width="20" height="18" viewBox="0 0 20 18"><rect x="1" y="4" width="13" height="13" fill="none" stroke="#16364a" stroke-width="2"/><path d="M4 9l4 4 10-12" fill="none" stroke="#16364a" stroke-width="3"/></svg>Online Marketing</li>
    <li><svg width="20" height="18" viewBox="0 0 20 18"><rect x="1" y="4" width="13" height="13" fill="none" stroke="#16364a" stroke-width="2"/><path d="M4 9l4 4 10-12" fill="none" stroke="#16364a" stroke-width="3"/></svg>Dashboard Controls</li>
    <li><svg width="20" height="18" viewBox="0 0 20 18"><rect x="1" y="4" width="13" height="13" fill="none" stroke="#16364a" stroke-width="2"/><path d="M4 9l4 4 10-12" fill="none" stroke="#16364a" stroke-width="3"/></svg>Full Setup and Support</li>
  </ul>
  <h1 class="abs hero-title"><b>Getting a website has</b><br><span>never been so simple</span></h1>
  <span class="abs signup">Sign up Now its</span>
  <span class="abs free-btn">FREE</span>
  <div class="abs showcase">
    <div class="showcase-art" role="img" aria-label="Illustration of laptops linked to a globe and a currency sign"></div>
    <h2>The Complete<br>Online Marketing Solution for<br>Small Business Websites</h2>
    <p>Get a big online presence<br>and more sales leads in 30 minutes</p>
  </div>
</section>

<h2 class="abs section-title">Stunning Business Websites</h2>
<svg class="abs arrow" style="left:35px" width="16" height="26" viewBox="0 0 16 26"><path d="M13 2L3 13l10 11" fill="none" stroke="#666" stroke-width="3"/></svg>
<svg class="abs arrow" style="left:688px" width="16" height="26" viewBox="0 0 16 26"><path d="M3 2l10 11L3 24" fill="none" stroke="#666" stroke-width="3"/></svg>
<div class="abs thumb" style="left:55px"><div role="img" aria-label="Business website template preview" style="background:linear-gradient(#3a3a3a 0 40%,#f1f1f1 40%)"></div></div>
<div class="abs thumb" style="left:216px"><div role="img" aria-label="Health website template preview" style="background:linear-gradient(#6aa6d8 0 40%,#f4f6f9 40%)"></div></div>
<div class="abs thumb" style="left:378px"><div role="img" aria-label="Dark technology website template preview" style="background:linear-gradient(90deg,#222 0 8%,#e8e6d6 8% 92%,#222 92%)"></div></div>
<div class="abs thumb" style="left:540px"><div role="img" aria-label="Dance studio website template preview" style="background:linear-gradient(#7a5ca8 0 5%,#f7f4fa 5%)"></div></div>
<p class="abs quote"><strong><span class="mark">“</span>Lorem Ipsum is simply dummy</strong> text of the printing and typesetting industry. Lorem Ipsum has been the industry's standard dummy text ever since the 1500s, when an unknown printer took a galley <span class="mark">”</span></p>

<div class="abs offer" style="left:34px;background:var(--grey-card)">
  <div class="price">£199<small>Value</small></div>
  <div class="badge" style="left:32px;top:20px;width:70px;height:50px;font-size:26px;background:transparent">FREE</div>
  <div class="headline" style="left:46px;top:58px;font-size:44px">Setup</div>
  <div class="band" style="font-size:18px">Web offer only</div>
</div>
<div class="abs offer" style="left:259px;background:var(--purple)">
  <div class="price">£22<small>per month</small></div>
  <div class="badge" style="left:14px;top:40px;width:60px;height:60px;font-size:12px">PRO<br>PACKAGE</div>
  <div class="headline" style="left:82px;top:52px;font-size:22px;line-height:24px;color:#9fd04a">Big online<br><span style="color:#fff;font-size:25px">presence</span></div>
  <div class="band">Business Website &amp; Easy Dashboard</div>
</div>
<div class="abs offer" style="left:486px;background:var(--green)">
  <div class="price">£29<small>per month</small></div>
  <div class="badge" style="left:8px;top:40px;width:62px;height:62px;font-size:11px">TURBO<br>SALES<br>PRO PLUS</div>
  <div class="headline" style="left:74px;top:52px;font-size:23px;line-height:26px;color:#6c9c2c">More sales<br><span style="color:#fff;font-size:30px;padding-left:18px">leads</span></div>
  <div class="band">Business Website, Easy Dashboard<br>&amp;PPC Sales</div>
</div>
<div class="abs how">
  <h3>How dose It work</h3>
  <p>Lorem Ipsum has been the industry's standard dummy text ever since the 1500s, when an unknown printer</p>
</div>

<section class="features">
  <div class="abs card" style="left:34px">
    <svg class="icon" width="24" height="24" viewBox="0 0 24 24"><rect x="4" y="5" width="14" height="16" fill="none" stroke="#555" stroke-width="2"/><path d="M7 10h8M7 14h8" stroke="#7b2a8c" stroke-width="2"/></svg>
    <h4>Case Studies</h4><p>Read real stories about small Business</p><a href="#">view more</a>
  </div>
  <div class="abs card" style="left:262px">
    <svg class="icon" width="24" height="24" viewBox="0 0 24 24"><circle cx="12" cy="12" r="11" fill="#888"/><path d="M9 8a3 3 0 1 1 6 1c0 2-2 2-2 4v2h-2v-2" fill="#fff"/></svg>
    <h4>How to</h4><p>Learn from our online marketing tips for small Business</p><a href="#">view more</a>
  </div>
  <div class="abs card" style="left:491px">
    <svg class="icon" width="28" height="28" viewBox="0 0 28 28"><rect x="3" y="4" width="22" height="20" rx="2" fill="#cfd8e0"/><circle cx="12" cy="16" r="7" fill="#2a8fd0"/></svg>
    <h4 style="left:63px">News &amp; Chatter</h4><p>Get Up-to-date news and chatter about online marketing</p><a href="#">view more</a>
  </div>
  <div class="abs card" style="left:719px">
    <svg class="icon" width="30" height="30" viewBox="0 0 30 30"><circle cx="15" cy="15" r="14" fill="#1c9ad6"/><circle cx="15" cy="15" r="9" fill="#fff"/><path d="M11 10l9 5-9 5z" fill="#1c9ad6"/></svg>
    <h4>Demo</h4><p>Find out what zVerda can do for your business</p><a href="#">view more</a>
  </div>
</section>

<footer class="footer">
  <ul class="abs fcol" style="left:44px"><li>Search Marketing</li><li style="line-height:12px;margin-bottom:5px">Organinc/ Natural (SEO)</li><li style="line-height:24px">Social Media</li><li>Web Analytics</li></ul>
  <ul class="abs fcol" style="left:258px"><li>Contact us</li><li>Customer Support</li><li>Request a Call Back</li><li>FAQ's</li></ul>
  <ul class="abs fcol" style="left:451px"><li>Sitemap</li><li>Termes &amp; Conditions</li><li>Privacy Policy</li></ul>
  <span class="abs news-label">Sign up for Newsletter</span>
  <div class="abs news-input">enter your email ID</div>
  <svg class="abs news-go" width="22" height="22" viewBox="0 0 22 22"><circle cx="11" cy="11" r="11" fill="#666"/><path d="M5 11h11M12 7l4 4-4 4" fill="none" stroke="#333" stroke-width="2"/></svg>
  <span class="abs social" style="left:822px;background:#111"></span>
  <span class="abs social" style="left:849px;background:#3fb0e6"></span>
  <span class="abs social" style="left:875px;background:#3b66b0"></span>
  <span class="abs social" style="left:901px;background:#f08a24"></span>
  <div class="abs rule"></div>
  <p class="abs copyright">All Rights Reserved, 2012 zVerda</p>
</footer>

</body>
</html>
```